Loud Kite Promotional Banner

We are looking for a design for a 33.5" x 79" retractable pop-up banners to used at our live shows. We are a cover band that performs at clubs, corporate events, private parties, and weddings. We would have 2 banners, one on each side of the drum riser, and placed between the lighting trusses. Our website and Social page will provide information on what we are about - high energy fun entertainment of live music. We would like some marketing on the banner with logos, etc - something classy that can be used at almost any event. Contact information on the banners would be great. The banners do not have to be the exact same.

Website: www. loudkiteband.example
FB: https://www.social.example/Loudkitebandplano

I have uploaded a logo that can be used. Any other information, images, etc are available not the sites too.

Target Market(s)

New clients looking for a live band

Industry/Entity Type

Live Entertainment

Colors
0054AA
0677BA
7BADD7
CADEEF
E8F1F8
0094D4
00A9DD
6FCCEA
C7EBF8
E9F6FB

Requirements
Must have
• Logo, website address
Nice to have
• Images and excitement

```html
<!DOCTYPE html>
<html lang="en">
<head>
<meta charset="utf-8">
<title>Loud Kite Banners</title>
<link rel="stylesheet" href="https://fonts.googleapis.com/css2?family=Lora:wght@700&display=swap">
<style>
  :root{
    --page:#dcdcdc;
    --banner-black:#000000;
    --ink-white:#ffffff;
    --navy:#1b1d4a;
    --magenta:#c0108f;
    --violet:#7a2ad0;
    --blue:#2f45d8;
    --red:#e0201c;
    --cyan:#1a7cff;
    --social-blue:#3361a8;
    --clips-red:#e02a20;
  }
  *{margin:0;padding:0;box-sizing:border-box}
  html,body{width:1200px;height:1200px;overflow:hidden;background:var(--page)}
  .stage{position:relative;width:1200px;height:1200px}
  .banner{position:absolute;top:151px;width:507px;height:874px;background:var(--banner-black);overflow:hidden;font-family:"Lora",Georgia,serif}
  .banner--left{left:81px}
  .banner--right{left:631px}
  .banner__art{position:absolute;inset:0 0 107px 0;
    background:
      radial-gradient(circle at 50% 46%, transparent 0 70px, rgba(192,16,143,.85) 75px, rgba(122,42,208,.6) 150px, transparent 230px),
      radial-gradient(ellipse 60% 30% at 0% 100%, rgba(224,32,28,.55), transparent 70%),
      linear-gradient(35deg, transparent 60%, rgba(26,124,255,.35) 78%, transparent 90%),
      var(--banner-black);}
  .banner__site{position:absolute;top:52px;left:0;right:0;text-align:center;color:var(--ink-white);font-size:28px;letter-spacing:4.5px;font-weight:700}
  .banner__name{position:absolute;top:360px;left:0;right:0;text-align:center;color:var(--ink-white);font-size:60px;font-weight:700;letter-spacing:3px}
  .banner__footer{position:absolute;left:0;right:0;bottom:0;height:107px;background:var(--ink-white)}
  .banner__socials{position:absolute;top:741px;left:0;right:0;display:flex;justify-content:center;gap:12px}
  .social{display:flex;align-items:center;gap:6px;background:var(--ink-white);border-radius:28px;padding:3px 12px 3px 3px;color:var(--navy);font-size:16px;font-weight:700}
  .social__dot{width:46px;height:46px;border-radius:50%;display:block}
  .social__dot--social{background:var(--social-blue)}
  .social__dot--clips{background:var(--clips-red)}
  .banner__handle{position:absolute;top:808px;left:0;right:0;text-align:center;color:var(--navy);font-size:28px;font-weight:700;letter-spacing:9px}
</style>
</head>
<body>
<div class="stage">
  <section class="banner banner--left">
    <div class="banner__art" role="img" aria-label="Glowing equalizer burst in magenta and blue over a dark hexagon mesh, with a cassette tape at its centre"></div>
    <p class="banner__site">www.loudkiteband.example</p>
    <p class="banner__name">Loud Kite</p>
    <div class="banner__footer"></div>
    <div class="banner__socials">
      <span class="social"><span class="social__dot social__dot--social"></span>Social</span>
      <span class="social"><span class="social__dot social__dot--clips"></span>Clips</span>
    </div>
    <p class="banner__handle">/Loudkitebandplano</p>
  </section>
  <section class="banner banner--right">
    <div class="banner__art" role="img" aria-label="Glowing equalizer burst in magenta and blue over a dark hexagon mesh, with a cassette tape at its centre"></div>
    <p class="banner__site">www.loudkiteband.example</p>
    <p class="banner__name">Loud Kite</p>
    <div class="banner__footer"></div>
    <div class="banner__socials">
      <span class="social"><span class="social__dot social__dot--social"></span>Social</span>
      <span class="social"><span class="social__dot social__dot--clips"></span>Clips</span>
    </div>
    <p class="banner__handle">/Loudkitebandplano</p>
  </section>
</div>
</body>
</html>
```